HARD MONEY ORIGINATOR RECRUITMENT.
Looking for individuals to help us originate loans for real estate investor financing primarily used to fix up properties and resell.
HARD MONEY ORIGINATORS WANTED
No Licensing Required
Work As Independent Contractor
1% Flat Finders Fee on Each Loan
Referral Compensation for Recruiting New Originators
Immediate Payouts
Programs Offered Nationwide
Marketing Assistance and Support Available
Email mbelton@corvalendgroup.com for more information or call (800) 641-2957 Ext. 24 Corva Lend Group Services, Inc. www.corvalendgroup.com NMLS #731864
Industry/Entity Type
Real Estate
Look and feel

```html
<!DOCTYPE html>
<html lang="en">
<head>
<meta charset="utf-8">
<title>Hard Money Originators Wanted</title>
<link href="https://fonts.googleapis.com/css2?family=Oswald:wght@300;400&family=Sancreek&display=swap" rel="stylesheet">
<style>
  :root {
    --backdrop: #ffffff;
    --paper: #f1e4cf;
    --tan: #d3a46d;
    --cream: #f5e8d4;
    --cream-soft: rgba(247, 235, 216, 0.82);
    --taupe: #a5997e;
    --photo-light: #d9c99a;
    --photo-dark: #9c8452;
  }
  html, body {
    margin: 0;
    width: 1200px;
    height: 1200px;
    overflow: hidden;
    background: var(--backdrop);
  }
  .poster {
    position: absolute;
    left: 195px;
    top: 30px;
    width: 810px;
    height: 1141px;
    background: var(--paper);
    font-family: "Oswald", sans-serif;
    font-weight: 300;
  }
  .poster-field {
    position: absolute;
    left: 22px;
    top: 25px;
    width: 763px;
    height: 1096px;
    background: var(--tan);
    overflow: hidden;
  }
  .poster-rule {
    position: absolute;
    inset: 14px;
    border: 2px solid var(--cream-soft);
  }
  .headline {
    position: absolute;
    top: 48px;
    left: 0;
    right: 0;
    text-align: center;
    color: var(--cream);
    font-size: 50px;
    letter-spacing: 6px;
    line-height: 1;
  }
  .wanted {
    position: absolute;
    top: 118px;
    left: 0;
    right: 0;
    text-align: center;
    color: var(--cream);
    font-family: "Sancreek", serif;
    font-size: 200px;
    line-height: 1;
    letter-spacing: 2px;
  }
  .stripes {
    position: absolute;
    left: 74px;
    width: 628px;
    background: var(--cream-soft);
  }
  .stripe-1 { top: 674px; height: 25px; }
  .stripe-2 { top: 723px; height: 13px; }
  .stripe-3 { top: 752px; height: 12px; }
  .stripe-4 { top: 782px; height: 7px; }
  .photo-ring {
    position: absolute;
    left: 142px;
    top: 318px;
    width: 490px;
    height: 490px;
    border-radius: 50%;
    background: var(--cream);
  }
  .photo {
    position: absolute;
    left: 152px;
    top: 328px;
    width: 470px;
    height: 470px;
    border-radius: 50%;
    background: radial-gradient(circle at 55% 40%, var(--photo-light), var(--photo-dark));
  }
  .brand-badge {
    position: absolute;
    left: 29px;
    top: 336px;
    width: 262px;
    height: 262px;
    border-radius: 50%;
    background: #f8f5ef;
    display: flex;
    align-items: center;
    justify-content: center;
    text-align: center;
  }
  .brand-name {
    width: 200px;
    color: var(--taupe);
    font-size: 26px;
    font-weight: 400;
    line-height: 1.15;
    text-transform: uppercase;
    letter-spacing: 1px;
  }
  .contact-badge {
    position: absolute;
    left: 481px;
    top: 547px;
    width: 246px;
    height: 246px;
    border-radius: 50%;
    background: var(--taupe);
    color: #f8f2e6;
    font-size: 15px;
    font-weight: 400;
    letter-spacing: 1.2px;
    text-transform: uppercase;
    text-align: center;
    line-height: 22px;
    display: flex;
    flex-direction: column;
    justify-content: center;
  }
  .contact-badge p { margin: 0; }
  .contact-badge .gap { margin-top: 22px; }
  .benefits {
    position: absolute;
    top: 812px;
    left: 0;
    right: 0;
    margin: 0;
    padding: 0;
    list-style: none;
    text-align: center;
    color: var(--cream-soft);
    font-size: 33px;
    line-height: 31px;
    letter-spacing: 1.5px;
    text-transform: uppercase;
  }
</style>
</head>
<body>
  <div class="poster">
    <div class="poster-field">
      <div class="poster-rule"></div>
      <div class="headline">HARD MONEY ORIGINATORS</div>
      <div class="wanted">WANTED</div>

      <div class="stripes stripe-1"></div>
      <div class="stripes stripe-2"></div>
      <div class="stripes stripe-3"></div>
      <div class="stripes stripe-4"></div>

      <div class="photo-ring"></div>
      <div class="photo" role="img" aria-label="Photo of construction workers in yellow hard hats and safety vests on a building site"></div>

      <div class="brand-badge">
        <div class="brand-name">Corva Lend Group Services, Inc.</div>
      </div>

      <div class="contact-badge">
        <p>(800) 641-2957 Ext. 24</p>
        <p class="gap">mbelton@corvalendgroup.com</p>
        <p>www.corvalendgroup.com</p>
        <p class="gap">Corva Lend Group</p>
        <p>Services, Inc.</p>
        <p>NMLS #731864</p>
      </div>

      <ul class="benefits">
        <li>No Licensing Required</li>
        <li>Work As Independent Contractor</li>
        <li>1% Flat Finders Fee On Each Loan</li>
        <li>Referral Compensation For Recruiting</li>
        <li>New Originators</li>
        <li>Immediate Payouts</li>
        <li>Programs Offered Nationwide</li>
        <li>Marketing Assistance And Support Available</li>
      </ul>
    </div>
  </div>
</body>
</html>
```